Tellwick Asset Management - Corporate Letter Head Project

Looking for a classy design based on our current logo. Please find current logo source file in files. With our color scheme.

Target Market(s)

We're an investment firm, the letterhead needs to look professional and attractive to clients.

Industry/Entity Type

Hedgefund

Colors
0054AA
0677BA
7BADD7
CADEEF
E8F1F8

Requirements
Must have
• Our logo, address, phone number, and email

```html
<!DOCTYPE html>
<html lang="en">
<head>
<meta charset="utf-8">
<title>Tellwick Asset Management Letterhead</title>
<link rel="stylesheet" href="https://fonts.googleapis.com/css2?family=Arimo&family=Montserrat:wght@400;600&family=Libre+Baskerville&display=swap">
<style>
  :root {
    --backdrop: #aaaaaa;
    --paper: #ffffff;
    --navy: #14305a;
    --ink: #555555;
    --ink-dark: #4a4a4a;
    --rule: #9a9a9a;
  }
  html, body { margin: 0; padding: 0; overflow: hidden; }
  body { width: 963px; height: 1200px; background: var(--backdrop); position: relative; }
  .letterhead {
    position: absolute; left: 130px; top: 94px; width: 703px; height: 994px;
    background: var(--paper); overflow: hidden;
    box-shadow: 2px 3px 6px rgba(0,0,0,.35);
  }
  .brand-mark {
    position: absolute; left: 96px; top: 40px; width: 50px; height: 50px;
    border: 1.5px solid var(--navy); box-sizing: border-box;
  }
  .brand-name {
    position: absolute; left: 52px; top: 102px; margin: 0;
    font-family: "Libre Baskerville", serif; font-weight: 400; color: var(--navy);
    font-size: 17px; line-height: 20px; letter-spacing: .2px;
  }
  .brand-name span { display: block; font-size: 8.5px; line-height: 11px; letter-spacing: 7.4px; }
  .contact {
    position: absolute; left: 518px; top: 45px; height: 73px; padding-left: 10px;
    border-left: 1px solid var(--rule); white-space: nowrap;
    font-family: "Montserrat", sans-serif; font-size: 11.5px; color: var(--ink); line-height: 14px;
    font-style: normal;
  }
  .contact p { margin: 0; }
  .contact .address { margin-bottom: 6px; }
  .contact .line { display: flex; align-items: center; gap: 5px; }
  .contact svg { width: 9px; height: 9px; fill: var(--navy); flex: none; }
  .letter { position: absolute; left: 52px; top: 305px; width: 578px; }
  .greeting {
    margin: 0 0 30px; font-family: "Montserrat", sans-serif; font-weight: 600;
    font-size: 15.5px; color: var(--ink-dark);
  }
  .body-copy p {
    margin: 0 0 13px; font-family: "Arimo", sans-serif; font-size: 12.2px;
    line-height: 14.3px; color: var(--ink);
  }
  .closing {
    margin: 25px 0 0; font-family: "Montserrat", sans-serif; font-weight: 600;
    font-size: 9px; color: var(--ink-dark);
  }
  .signature {
    margin-top: 30px; width: 86px; height: 24px;
    background: linear-gradient(90deg, #e9e9e9, #f3f3f3);
  }
  .footer-swoosh { position: absolute; left: 0; bottom: 0; width: 703px; height: 60px; display: block; }
</style>
</head>
<body>
  <main class="letterhead">
    <div class="brand-mark"></div>
    <h1 class="brand-name">TELLWICK ASSET<span>MANAGEMENT</span></h1>

    <address class="contact">
      <p class="address">Your address, city<br>state, ZIP 0000</p>
      <p class="line"><svg viewBox="0 0 10 10"><path d="M2 1l2 2-1 1.3c.6 1.2 1.5 2.1 2.7 2.7L7 6l2 2-1.2 1.3C4.5 9 1 5.5.7 2.2z"/></svg>123-456-2100</p>
      <p class="line"><svg viewBox="0 0 10 10"><path d="M0 2h10v6H0zM0 2l5 3.5L10 2"/></svg>youremail@twmail.com</p>
      <p class="line"><svg viewBox="0 0 10 10"><circle cx="5" cy="5" r="4.8"/></svg>www.yourwebsite.com</p>
    </address>

    <article class="letter">
      <p class="greeting">Dear Mr. Harlow,</p>
      <div class="body-copy">
        <p>Lorem ipsum dolor sit amet, consectetuer adipiscing elit, sed diam nonmmy nibh euismod tincidunt ut laor eet dolore magna aliquam erat volutpat. Ut wisi enim ad minim veniam, quis nostrud exerci tationmcorper suscipit lobortis nisl ut aliquip ex ea commodo consequat. Duis autem vel eum iriure dolor in hendrerit in vulputate velit esse molestie consequat, vel illum dolore eu feugiat</p>
        <p>Rorem ipsum dolor sit amet, consectetuer adipiscing elit, sed diam nonmmy nibh euismod tincidunt ut laor eet dolore magna aliquam erat volutpat. Ut wisi enim ad minim veniam, quis nostrud exerci tationmcorper suscipit lobortis nisl ut aliquip ex ea commodo consequat. Duis autem vel eum iriure dolor in hendrerit in vulputate velit esse molest</p>
        <p>Dorem ipsum dolor sit amet, consectetuer adipiscing elit, sed diam nonmmy nibh euismod tincidunt ut laor eet dolore magna aliquam erat volutpat. Ut wisi enim ad minim veniam, quis nostrud exerci tationmcorper suscipit lobortis nisl ut aliquip ex ea commodo consequat. Duis autem vel eum iriure dolor in hendrerit in suscipit lobortis nisl ut aliquip ex ea commodo consequat. Duis autem vel eum iriure dolor in hendrerit in vulputate velit esse molestie consequat, vel illum</p>
        <p>Sorem ipsum dolor sit amet, consectetuer adipiscing elit, sed diam nonmmy nibh euismod tincidunt ut laor eet dolore magna aliquam erat volutpat. Ut wisi enim ad minim veniam, quis nostrud exerci tationmcorper suscipit lobortis nisl ut aliquip ex ea commodo consequat. Duis autem vel eum iriure dolor in</p>
      </div>
      <p class="closing">Sincerely,</p>
      <div class="signature" role="img" aria-label="Handwritten signature of the sender"></div>
    </article>

    <svg class="footer-swoosh" viewBox="0 0 703 60" preserveAspectRatio="none" aria-hidden="true">
      <path d="M27 60 Q300 -2 703 8 L703 60 Z" fill="var(--navy)"/>
      <path d="M115 60 Q330 8 582 3 Q340 12 132 60 Z" fill="var(--paper)"/>
    </svg>
  </main>
</body>
</html>
```